Website Refresh for Niche Pet Website

We have a site that needs a fresh, modern look. This site gets approx 500K views a month and we want a re-design.

Category layout
New blog template layout

We need to keep the large rolling ads on the home page
The small ad need to be placed on the side when looking at the interior page.

We need a modern slick easy to use site

Target Market(s)

Breeders and pet buyers in the UK

Industry/Entity Type

pets

Number of Pages Required

4 page

Requirements
Must have
• Be Gun Dog specific - these are for working homes. Creative way to showcase the ads, breeds etc.
Nice to have
• We are open to logo improvements and colour, however, this is the UK market for buying and selling gun dogs. The grren and gold do work well.

```html
<!DOCTYPE html>
<html lang="en">
<head>
<meta charset="utf-8">
<title>Fieldline Hounds</title>
<link href="https://fonts.googleapis.com/css2?family=Russo+One&family=Roboto:wght@400;500;700&family=Montserrat:wght@800&family=Bitter:wght@500&display=swap" rel="stylesheet">
<style>
:root{
  --green:#4b5e2e;
  --gold:#d7a75c;
  --ink:#1e1e1e;
  --muted:#666;
  --line:#d8d8d8;
  --black:#000;
  --white:#fff;
}
*{box-sizing:border-box;margin:0;padding:0}
html,body{width:1200px;height:3723px;overflow:hidden}
body{position:relative;font-family:"Roboto",sans-serif;color:var(--ink);background:var(--white)}
.abs{position:absolute}
.display{font-family:"Russo One",sans-serif;text-transform:uppercase}

.topline{left:0;top:0;width:1200px;height:4px;background:var(--gold)}
.brand{left:112px;top:20px;width:200px;height:130px;display:flex;align-items:center;gap:10px;font-family:"Roboto",sans-serif;font-weight:700;font-size:24px;color:var(--green);line-height:1.05}
.brand-dot{width:28px;height:28px;border-radius:50%;background:var(--gold);flex:none}
.btn{display:inline-flex;align-items:center;justify-content:center;border-radius:22px;color:var(--white);font-weight:700;font-size:14px}
.btn-buy{left:820px;top:42px;width:128px;height:44px;background:var(--green)}
.btn-sell{left:962px;top:42px;width:128px;height:44px;background:var(--gold)}
.nav{top:106px;left:460px;width:632px;display:flex;justify-content:space-between;font-size:14px;font-weight:700}

.hero{left:0;top:169px;width:1200px;height:589px;background:linear-gradient(100deg,#4a3a28 0%,#8a6a45 35%,#e6c99a 60%,#b58f62 80%,#5a4630 100%)}
.hero-ring{left:104px;top:239px;width:450px;height:450px;border-radius:50%;background:var(--white)}
.hero-circle{left:113px;top:248px;width:432px;height:432px;border-radius:50%;background:var(--green);color:var(--white);text-align:center;overflow:hidden}
.hero-circle h1{margin-top:82px;font-family:"Russo One",sans-serif;font-size:37px;line-height:48px;font-weight:400}
.hero-circle p{margin:20px auto 0;width:360px;font-size:16px;line-height:29px}
.hero-cta{margin:22px auto 0;width:120px;height:42px;background:var(--gold);border-radius:21px;display:flex;align-items:center;justify-content:center;font-weight:700;font-size:14px}
.hero-art{left:205px;top:580px;width:240px;height:100px;background:rgba(255,255,255,.25);border-radius:120px 120px 0 0}

.cats{left:158px;top:826px;width:884px;display:flex;justify-content:space-between}
.cat{width:150px;text-align:center;font-size:16px;color:#333}
.cat-icon{width:78px;height:78px;margin:0 auto 16px;border-radius:50%;border:1px solid var(--line);display:flex;align-items:center;justify-content:center}

.sec-title{font-family:"Russo One",sans-serif;font-size:40px;text-transform:uppercase;color:var(--ink)}
.rec-title{left:0;top:1018px;width:1200px;text-align:center}
.rec-text{left:150px;top:1095px;width:900px;text-align:center;font-size:15px;line-height:29px;color:var(--muted)}

.card{top:1193px;width:316px}
.card-img{width:314px;height:392px}
.price{position:absolute;right:14px;top:374px;width:112px;height:34px;border-radius:17px;background:var(--gold);color:var(--white);font-size:13px;font-weight:500;display:flex;align-items:center;justify-content:center}
.card h3{margin-top:24px;margin-left:-6px;font-family:"Russo One",sans-serif;font-size:25px;font-weight:400}
.card .loc{margin-top:10px;margin-left:-6px;font-size:16px;color:#333}
.card .date{margin-top:12px;margin-left:-6px;font-size:13px;color:#333}
.card .view{margin-top:16px;margin-left:-6px;display:flex;align-items:center;gap:12px;font-size:13px;font-weight:500;padding-bottom:16px;border-bottom:1px solid var(--line)}
.card .arrow{width:26px;height:26px;border-radius:50%;border:1px solid var(--line);display:flex;align-items:center;justify-content:center}

.about-img{left:108px;top:1895px;width:488px;height:459px;background:linear-gradient(160deg,#a7a163 0%,#5d6c2b 50%,#3e4a1e 100%)}
.about-title{left:648px;top:1940px}
.about-text{left:648px;top:2005px;width:460px;font-size:13px;line-height:27.5px;color:var(--muted)}
.about-text p+p{margin-top:27px}

.how-panel{left:0;top:2490px;width:776px;height:506px;background:var(--green);border-radius:0 14px 14px 0}
.how-title{left:117px;top:2548px;color:var(--white)}
.how-arrows{left:645px;top:2556px;display:flex;gap:32px;color:var(--white);font-size:22px}
.how-video{left:117px;top:2627px;width:977px;height:481px;background:linear-gradient(180deg,#d9dadb 0%,#b7b0a0 55%,#6e5f47 100%);border-radius:4px}
.play{left:580px;top:2841px;width:52px;height:52px;border-radius:50%;background:var(--gold);display:flex;align-items:center;justify-content:center}

.banner{left:0;top:3230px;width:1200px;height:236px;background:#e4b94e;overflow:hidden}
.banner-photo{left:0;top:3230px;width:440px;height:236px;background:linear-gradient(120deg,#6b3b20,#b06a3a 55%,#7a8a4a);clip-path:polygon(0 0,100% 0,82% 100%,0 100%)}
.banner-name{left:440px;top:3232px;width:740px;text-align:center;font-family:"Montserrat",sans-serif;font-weight:800;font-size:64px;line-height:62px;color:#5a2410}
.banner-list{left:416px;top:3366px;width:784px;display:flex;justify-content:space-around;font-family:"Bitter",serif;font-weight:500;font-size:27px;color:#5a2410}
.banner-url{left:440px;top:3406px;width:740px;text-align:center;font-family:"Bitter",serif;font-weight:500;font-size:48px;letter-spacing:2px;color:#5a2410}

.footer{left:0;top:3466px;width:1200px;height:257px;background:var(--black)}
.footer-brand{left:110px;top:3530px;font-family:"Roboto",sans-serif;font-weight:700;font-size:28px;color:var(--gold);display:flex;align-items:center;gap:12px}
.footer-nav{left:460px;top:3538px;width:632px;display:flex;justify-content:space-between;font-size:14px;font-weight:700;color:var(--white)}
.social{left:912px;top:3590px;display:flex;gap:8px}
.social span{width:38px;height:38px;border-radius:50%;background:var(--gold)}
.copy{left:824px;top:3649px;font-size:14px;font-weight:700;color:var(--white)}
</style>
</head>
<body>
<div class="abs topline"></div>
<div class="abs brand"><span class="brand-dot"></span><span>Fieldline<br>Hounds</span></div>
<a class="abs btn btn-buy">Buy A Dog</a>
<a class="abs btn btn-sell">Sell A Dog</a>
<nav class="abs nav"><span>Home</span><span>Our Categories</span><span>How It Works</span><span>Reviews</span><span>About Us</span></nav>

<section class="abs hero" role="img" aria-label="Hunter with a shotgun walking a gun dog on a lead along a misty woodland path at sunrise"></section>
<div class="abs hero-ring"></div>
<div class="abs hero-circle">
  <h1>WELCOME TO<br>FIELDLINE HOUNDS</h1>
  <p>At vero eos et accusamus et iusto odio dignissimos ducimus qui blanditiis praesentium voluptatum deleniti atque co</p>
  <div class="hero-cta">Get Started</div>
</div>
<div class="abs hero-art" role="img" aria-label="White silhouette of a pointing dog among reeds with birds taking flight"></div>

<div class="abs cats">
  <div class="cat"><div class="cat-icon"><svg width="30" height="30" viewBox="0 0 30 30" fill="none" stroke="#333" stroke-width="1.5"><circle cx="15" cy="15" r="11"/><circle cx="11" cy="13" r="1"/><circle cx="19" cy="13" r="1"/><path d="M12 19q3 2 6 0"/></svg></div>Labrador</div>
  <div class="cat"><div class="cat-icon"><svg width="30" height="30" viewBox="0 0 30 30" fill="none" stroke="#333" stroke-width="1.5"><path d="M8 8q7-6 14 0v14q-7 5-14 0z"/><circle cx="12" cy="14" r="1"/><circle cx="18" cy="14" r="1"/></svg></div>Springer Spaniels</div>
  <div class="cat"><div class="cat-icon"><svg width="30" height="30" viewBox="0 0 30 30" fill="none" stroke="#333" stroke-width="1.5"><path d="M10 6q5-3 10 0l3 14q-8 6-16 0z"/><circle cx="12.5" cy="13" r="1"/><circle cx="17.5" cy="13" r="1"/></svg></div>Cocker Spaniels</div>
  <div class="cat"><div class="cat-icon"><svg width="30" height="30" viewBox="0 0 30 30" fill="none" stroke="#333" stroke-width="1.5"><path d="M8 5l4 6h6l4-6v12q-7 10-14 0z"/><circle cx="12.5" cy="15" r="1"/><circle cx="17.5" cy="15" r="1"/></svg></div>Lost/stolen Dogs</div>
  <div class="cat"><div class="cat-icon"><svg width="30" height="30" viewBox="0 0 30 30" fill="none" stroke="#333" stroke-width="1.5"><path d="M6 12q4-8 12-6l6 6-4 3h-6l-2 8H8z"/><circle cx="16" cy="11" r="1"/></svg></div>Events &amp; Trials</div>
  <div class="cat"><div class="cat-icon"><svg width="30" height="30" viewBox="0 0 30 30" fill="none" stroke="#333" stroke-width="1.5"><circle cx="15" cy="16" r="9"/><circle cx="8" cy="8" r="3"/><circle cx="22" cy="8" r="3"/><ellipse cx="15" cy="19" rx="3" ry="2"/></svg></div>Place An Advert</div>
</div>

<h2 class="abs sec-title rec-title">Recommended For You</h2>
<p class="abs rec-text">At vero eos et accusamus et iusto odio dignissimos ducimus qui blanditiis praesentium voluptatum deleniti atque corrupti quos dolores et quas molestias excepturi sint occaecati cupiditate non provident, similique sunt in culpa qui officia deserunt mol</p>

<article class="abs card" style="left:104px">
  <div class="card-img" role="img" aria-label="Litter of fox red Labrador puppies on a grey rug" style="background:linear-gradient(160deg,#c9c4bb,#c8914f 50%,#8d8478)"></div>
  <span class="price">£1200.00</span>
  <h3>Puppies</h3><p class="loc">County durham , Durham</p><p class="date">7th October 2023</p>
  <div class="view"><span class="arrow"><svg width="10" height="10" viewBox="0 0 10 10" fill="none" stroke="#333" stroke-width="1.3"><path d="M2 2l3 3-3 3M5 2l3 3-3 3"/></svg></span>View Details</div>
</article>
<article class="abs card" style="left:447px">
  <div class="card-img" role="img" aria-label="Liver and white springer spaniel sitting on grass" style="background:linear-gradient(160deg,#3f5a2a,#6b3f2c 50%,#6f8a3a)"></div>
  <span class="price">£2000.00</span>
  <h3>Kinross</h3><p class="loc">County durham , Durham</p><p class="date">6th October 2023</p>
  <div class="view"><span class="arrow"><svg width="10" height="10" viewBox="0 0 10 10" fill="none" stroke="#333" stroke-width="1.3"><path d="M2 2l3 3-3 3M5 2l3 3-3 3"/></svg></span>View Details</div>
</article>
<article class="abs card" style="left:788px">
  <div class="card-img" role="img" aria-label="Wet black cocker spaniel standing on stony ground" style="background:linear-gradient(160deg,#8a8374,#2a2a2a 50%,#9a9080)"></div>
  <span class="price">£1000.00</span>
  <h3>Puppies</h3><p class="loc">Torquay</p><p class="date">6th October 2023</p>
  <div class="view"><span class="arrow"><svg width="10" height="10" viewBox="0 0 10 10" fill="none" stroke="#333" stroke-width="1.3"><path d="M2 2l3 3-3 3M5 2l3 3-3 3"/></svg></span>View Details</div>
</article>

<div class="abs about-img" role="img" aria-label="Black Labrador retrieving a pheasant across a grassy field"></div>
<h2 class="abs sec-title about-title">About Us</h2>
<div class="abs about-text">
  <p>Our aim at FieldlineHounds has always been to provide the very best gundog advertisement platform to purchase and sell your gundogs in the safest possible way. FieldlineHounds was created by gundog people that know your time is valuable and best spent in the field with your dogs, thats why we have no lengthy registration forms to fill in or no accounts to remember passwords for adverts you posted 3 months ago.</p>
  <p>Here at FieldlineHounds your advert stays on until sold and all we ask in return is that you keep your advert updated with our email edit links so our customers looking to purchase their new gun dog can make the best informed decisions.</p>
</div>

<div class="abs how-panel"></div>
<h2 class="abs sec-title how-title">How It Works</h2>
<div class="abs how-arrows"><span>«</span><span>»</span></div>
<div class="abs how-video" role="img" aria-label="Wildfowler in camouflage holding a shotgun as a black Labrador leaps through reeds"></div>
<div class="abs play"><svg width="16" height="16" viewBox="0 0 16 16"><circle cx="8" cy="8" r="7" fill="none" stroke="#fff" stroke-width="1.5"/><path d="M6.5 5v6l4.5-3z" fill="#fff"/></svg></div>

<div class="abs banner"></div>
<div class="abs banner-photo" role="img" aria-label="Close-up of a fox red Labrador's head"></div>
<div class="abs banner-name">BRYNCOED<br>RETRIEVERS</div>
<div class="abs banner-list"><span>• Qualified &amp; Licensed Breeder</span><span>• Stud Dogs</span><span>• Part Trained Dogs</span></div>
<div class="abs banner-url">bryncoedretrievers.co.uk</div>

<footer class="abs footer"></footer>
<div class="abs footer-brand"><span class="brand-dot"></span>Fieldline Hounds</div>
<nav class="abs footer-nav"><span>Home</span><span>Our Categories</span><span>How It Works</span><span>Reviews</span><span>About Us</span></nav>
<div class="abs social"><span></span><span></span><span></span><span></span></div>
<p class="abs copy">© Copyright 2023 | All rights Reserved</p>
</body>
</html>
```